Stationary Design for Stunning new Logo

I need to envelopes, letterhead, business cards designed to compliment our new logo.

We are a 25 year old printing company going through a brand refresh. All items should have the design extended to both sides for full print ability.

Industry/Entity Type

Printing

Requirements
Must have
• It must utilize the new logo & colors PMS 300 & PMS 295.

```html
<!DOCTYPE html>
<html lang="en">
<head>
<meta charset="utf-8">
<title>Norapress Stationery Set</title>
<link href="https://fonts.googleapis.com/css2?family=Roboto+Condensed:wght@400;700&family=Roboto:wght@700&display=swap" rel="stylesheet">
<style>
  :root{
    --navy:#003a70;
    --blue:#0067c5;
    --paper:#ffffff;
    --ink:#222222;
    --bg-light:#767676;
    --bg-dark:#3a3a3a;
    --deco:#cfe0f3;
  }
  *{margin:0;padding:0;box-sizing:border-box}
  html,body{width:1200px;height:1000px;overflow:hidden}
  body{
    position:relative;
    background:radial-gradient(ellipse at 45% 45%,var(--bg-light) 0%,var(--bg-dark) 100%);
    font-family:"Roboto Condensed",Arial,sans-serif;
    color:var(--ink);
  }
  .sheet{position:absolute;background:var(--paper);overflow:hidden}

  .brand{position:absolute;white-space:nowrap}
  .brand-mark{display:inline-block;border-radius:50%;background:var(--blue);vertical-align:middle}
  .brand-name{font-family:"Roboto Condensed",sans-serif;font-weight:700;color:var(--blue);vertical-align:middle;letter-spacing:.02em}
  .brand-tagline{display:block;color:var(--blue);font-family:"Roboto Condensed",sans-serif;font-weight:400;letter-spacing:.01em}

  /* Letterhead */
  .letterhead{left:48px;top:18px;width:524px;height:726px}
  .letterhead .brand{left:22px;top:16px}
  .letter-body{position:absolute;left:23px;top:112px;width:486px;font-size:9.1px;line-height:9.8px;color:#222}
  .letter-body p{margin-bottom:19px}
  .letter-body p:nth-child(2){margin-bottom:29px}
  .signature{position:absolute;left:28px;top:490px;width:100px;height:48px;background:linear-gradient(90deg,#e4eef9,#f3f7fc);border-radius:4px}
  .signer{position:absolute;left:30px;top:544px}
  .signer-name{font-family:Roboto,Arial,sans-serif;font-weight:700;font-size:12.5px;color:var(--navy);line-height:14px}
  .signer-role{font-family:Roboto,Arial,sans-serif;font-weight:700;font-size:10px;color:var(--blue);line-height:12px}
  .contacts{position:absolute;list-style:none}
  .contacts li{display:flex;align-items:center;height:15.5px;font-family:Roboto,Arial,sans-serif;font-weight:700;font-size:9.6px;color:var(--navy)}
  .contacts .icon{width:12px;height:12px;background:var(--blue);margin-right:11px;display:flex;align-items:center;justify-content:center;flex:none}
  .letterhead .contacts{left:22px;top:670px}
  .deco-circle{position:absolute;border-radius:50%;border:14px solid var(--deco)}

  /* Envelope back panel (tall) */
  .folder{left:628px;top:18px;width:517px;height:720px;border-radius:18px 18px 0 0}
  .folder-band{position:absolute;left:0;top:0;width:100%;height:59px;background:var(--navy)}
  .folder .brand{left:17px;top:103px}

  /* Business cards */
  .card{box-shadow:0 2px 6px rgba(0,0,0,.45)}
  .card-front{left:725px;top:206px;width:320px;height:206px}
  .card-front .brand{left:30px;top:78px}
  .card-front .band-dark{position:absolute;left:0;top:159px;width:100%;height:5px;background:var(--navy)}
  .card-front .band-blue{position:absolute;left:0;top:164px;width:100%;height:42px;background:var(--blue)}

  .card-back{left:725px;top:433px;width:325px;height:208px}
  .card-stripe{position:absolute;left:25px;top:0;width:45px;height:100%;background:var(--blue)}
  .card-stripe-disc{position:absolute;left:22px;top:30px;width:51px;height:72px;border-radius:0 0 26px 26px;background:var(--paper);border:3px solid var(--blue)}
  .card-back .brand{left:83px;top:40px}
  .card-back .signer{left:84px;top:96px}
  .card-back .contacts{left:85px;top:138px}

  /* Envelope front */
  .envelope-front{left:48px;top:765px;width:525px;height:203px}
  .envelope-front .brand{left:17px;top:22px}
  .address-fields{position:absolute;left:305px;top:65px;list-style:none}
  .address-fields li{display:flex;align-items:flex-end;height:19.5px;font-family:Roboto,Arial,sans-serif;font-weight:700;font-size:9.6px;color:var(--navy)}
  .address-fields .label{width:60px}
  .address-fields .rule{width:97px;border-bottom:1.5px solid var(--blue);margin-bottom:3px}
  .envelope-front .band-dark{position:absolute;left:0;top:171px;width:100%;height:6px;background:var(--navy)}
  .envelope-front .band-blue{position:absolute;left:0;top:177px;width:100%;height:26px;background:var(--blue)}

  /* Envelope back */
  .envelope-back{left:620px;top:765px;width:525px;height:203px}
  .envelope-flap{position:absolute;left:0;top:0}
  .envelope-back .brand{left:388px;top:178px}
</style>
</head>
<body>

<section class="sheet letterhead">
  <div class="brand">
    <span class="brand-mark" style="width:24px;height:24px;margin-right:6px"></span><span class="brand-name" style="font-size:26px">NORAPRESS</span>
    <span class="brand-tagline" style="font-size:6.6px;margin-left:30px;margin-top:-3px">OUTSTANDING SERVICE • QUALITY PRODUCT • COMPETITIVE PRICING.</span>
  </div>
  <div class="letter-body">
    <p>A letterhead is the heading at the top of a sheet of letter paper (stationery). That heading usually consists of a name and an address, and a logo or corporate design, and sometimes a background pattern. The term "letterhead" is often used to refer to the whole sheet imprinted with such a heading.The majority of company letterheads are printed A4 in size (210mm x 297mm) although occasionally A5 (148mm x 210mm) and other bespoke sizes are sometimes used. [citation needed] Certain pieces of information are required to be displayed by law for UK based limited companies. The company name must be included, the place of registration, the registered number and the address of the registered office</p>
    <p>A letterhead is the heading at the top of a sheet of letter paper (stationery). That heading usually consists of a name and an address, and a logo or corporate design, and sometimes a background pattern. The term "letterhead" is often used to refer to the whole sheet imprinted with such a heading.The majority of company letterheads are printed A4 in size (210mm x 297mm) although occasionally A5 (148mm x 210mm) and other bespoke sizes are sometimes used. [citation needed] Certain pieces of information are required to be displayed by law for UK based limited companies. The company name must be included, the place of registration, the registered number and the address of the registered office</p>
    <p>A letterhead is the heading at the top of a sheet of letter paper (stationery). That heading usually consists of a name and an address, and a logo or corporate design, and sometimes a background pattern. The term "letterhead" is often used to refer to the whole sheet imprinted with such a heading.The majority of company letterheads are printed A4 in size (210mm x 297mm) although occasionally A5 (148mm x 210mm) and other bespoke sizes are sometimes used. [citation needed] Certain pieces of information are required to be displayed by law for UK based limited companies. The company name must be included, the place of registration, the registered number and the address of the registered office</p>
    <p>A letterhead is the heading at the top of a sheet of letter paper (stationery). That heading usually consists of a name and an address, and a logo or corporate design, and sometimes a background pattern. The term "letterhead" is often used to refer to the whole sheet imprinted with such a heading.The majority of company letterheads are printed A4 in size (210mm x 297mm) although occasionally A5 (148mm x 210mm) and other bespoke sizes are sometimes used. [citation needed] Certain pieces of information are required to be displayed by law for UK based limited companies. The company name must be included, the place of registration, the registered number and the address of the registered office</p>
  </div>
  <div class="signature" role="img" aria-label="Handwritten signature"></div>
  <div class="signer">
    <div class="signer-name">YOUR NAME</div>
    <div class="signer-role">OWNER</div>
  </div>
  <ul class="contacts">
    <li><span class="icon"><svg width="8" height="8" viewBox="0 0 8 8"><path d="M1.5 0.5 L3 0.5 L3.5 2.3 L2.6 3 Q3.4 4.8 5 5.4 L5.7 4.5 L7.5 5 L7.5 6.5 Q4 7.5 1 3.5 Q0.5 1.5 1.5 0.5Z" fill="#fff"/></svg></span>+123 456 7890</li>
    <li><span class="icon"><svg width="9" height="7" viewBox="0 0 9 7"><rect x="0.5" y="0.5" width="8" height="6" fill="none" stroke="#fff"/><path d="M0.5 0.5 L4.5 4 L8.5 0.5" fill="none" stroke="#fff"/></svg></span>YOURNAME@NORAPRESS.COM</li>
    <li><span class="icon"><svg width="9" height="9" viewBox="0 0 9 9"><circle cx="4.5" cy="4.5" r="3.8" fill="none" stroke="#fff" stroke-width=".8"/><ellipse cx="4.5" cy="4.5" rx="1.6" ry="3.8" fill="none" stroke="#fff" stroke-width=".8"/><path d="M0.7 4.5 H8.3" stroke="#fff" stroke-width=".8"/></svg></span>WWW.NORAPRESS.COM</li>
  </ul>
  <div class="deco-circle" style="left:414px;top:617px;width:110px;height:110px"></div>
</section>

<section class="sheet folder">
  <div class="folder-band"></div>
  <div class="brand">
    <span class="brand-mark" style="width:40px;height:40px;margin-right:8px"></span><span class="brand-name" style="font-size:38px">NORAPRESS</span>
    <span class="brand-tagline" style="font-size:9.4px;margin-left:50px;margin-top:-4px">OUTSTANDING SERVICE • QUALITY PRODUCT • COMPETITIVE PRICING.</span>
  </div>
  <div class="deco-circle" style="left:412px;top:617px;width:100px;height:100px"></div>
</section>

<section class="sheet card card-front">
  <div class="brand">
    <span class="brand-mark" style="width:26px;height:26px;margin-right:6px"></span><span class="brand-name" style="font-size:28px">NORAPRESS</span>
    <span class="brand-tagline" style="font-size:7px;margin-left:34px;margin-top:-3px">OUTSTANDING SERVICE • QUALITY PRODUCT • COMPETITIVE PRICING.</span>
  </div>
  <div class="band-dark"></div>
  <div class="band-blue"></div>
</section>

<section class="sheet card card-back">
  <div class="card-stripe"></div>
  <div class="card-stripe-disc"></div>
  <div class="brand">
    <span class="brand-name" style="font-size:25px">NORAPRESS</span>
    <span class="brand-tagline" style="font-size:6.6px;margin-top:-3px">OUTSTANDING SERVICE • QUALITY PRODUCT • COMPETITIVE PRICING.</span>
  </div>
  <div class="signer">
    <div class="signer-name" style="font-size:13px">YOUR NAME</div>
    <div class="signer-role">OWNER</div>
  </div>
  <ul class="contacts">
    <li><span class="icon"><svg width="8" height="8" viewBox="0 0 8 8"><path d="M1.5 0.5 L3 0.5 L3.5 2.3 L2.6 3 Q3.4 4.8 5 5.4 L5.7 4.5 L7.5 5 L7.5 6.5 Q4 7.5 1 3.5 Q0.5 1.5 1.5 0.5Z" fill="#fff"/></svg></span>+123 456 7890</li>
    <li><span class="icon"><svg width="9" height="7" viewBox="0 0 9 7"><rect x="0.5" y="0.5" width="8" height="6" fill="none" stroke="#fff"/><path d="M0.5 0.5 L4.5 4 L8.5 0.5" fill="none" stroke="#fff"/></svg></span>YOURNAME@NORAPRESS.COM</li>
    <li><span class="icon"><svg width="9" height="9" viewBox="0 0 9 9"><circle cx="4.5" cy="4.5" r="3.8" fill="none" stroke="#fff" stroke-width=".8"/><ellipse cx="4.5" cy="4.5" rx="1.6" ry="3.8" fill="none" stroke="#fff" stroke-width=".8"/><path d="M0.7 4.5 H8.3" stroke="#fff" stroke-width=".8"/></svg></span>WWW.NORAPRESS.COM</li>
  </ul>
</section>

<section class="sheet envelope-front">
  <div class="brand">
    <span class="brand-mark" style="width:24px;height:24px;margin-right:6px"></span><span class="brand-name" style="font-size:25px">NORAPRESS</span>
    <span class="brand-tagline" style="font-size:6.6px;margin-left:30px;margin-top:-3px">OUTSTANDING SERVICE • QUALITY PRODUCT • COMPETITIVE PRICING.</span>
  </div>
  <ul class="address-fields">
    <li><span class="label">RECEPIENT:</span><span class="rule"></span></li>
    <li><span class="label">ADDRESS:</span><span class="rule"></span></li>
    <li><span class="label">CITY:</span><span class="rule"></span></li>
    <li><span class="label">COUNTRY:</span><span class="rule"></span></li>
  </ul>
  <div class="band-dark"></div>
  <div class="band-blue"></div>
</section>

<section class="sheet envelope-back">
  <svg class="envelope-flap" width="525" height="100" viewBox="0 0 525 100">
    <path d="M0 0 H525 L295 84 Q262 96 229 84 Z" fill="var(--blue)"/>
  </svg>
  <div class="brand">
    <span class="brand-mark" style="width:13px;height:13px;margin-right:3px"></span><span class="brand-name" style="font-size:14px">NORAPRESS</span>
    <span class="brand-tagline" style="font-size:4px;margin-left:16px;margin-top:-2px">OUTSTANDING SERVICE • QUALITY PRODUCT • COMPETITIVE PRICING.</span>
  </div>
</section>

</body>
</html>
```